National online rug retailer needs a home page design

See the LoomNest logo and create a home page design around that color theme. Details are spelled out in word document uploaded below.
Updates

Apparently this website did not take my attachement showing the logo and basic requirements.  If you would send me your email address, I will send you the attachment directly.
Best regards,
Ned Carver
ncarver@qwplex.com

Target Market(s)

The target market is home owners 25 to 75 years old with combined incomes over $100,000 per year.

Industry/Entity Type

Online

Requirements
Must have
• Lots of white space with black letters and creative use of red and possibly one other color. Would like a compelling call to action button.

```html
<!DOCTYPE html>
<html lang="en">
<head>
<meta charset="utf-8">
<title>LoomNest — Home</title>
<link href="https://fonts.googleapis.com/css2?family=Open+Sans:wght@400;600;700&display=swap" rel="stylesheet">
<style>
:root{
  --red:#e31b23;
  --red-dark:#b9121a;
  --ink:#222;
  --muted:#555;
  --line:#dcdcdc;
  --nav:#505050;
  --backdrop:#ececec;
  --panel:#f1f1f1;
  --foot:#474747;
}
*{margin:0;padding:0;box-sizing:border-box}
html,body{width:810px;height:1200px;overflow:hidden}
body{background:var(--backdrop);font-family:"Open Sans",Arial,sans-serif;color:var(--ink);position:relative}
.page{position:absolute;left:81px;top:0;width:653px;height:1200px;background:#fff}
.abs{position:absolute}
/* header */
.wordmark{left:90px;top:28px;font-size:28px;font-weight:600;color:var(--red);letter-spacing:-.5px;line-height:34px}
.search{left:330px;top:34px;width:151px;height:24px;border:1px solid #bbb;font-size:7.5px;color:#999;padding:6px 7px}
.search-btn{left:483px;top:34px;width:24px;height:24px;background:#666}
.topinfo{left:540px;width:182px;text-align:right;font-size:8px;color:#555}
.topinfo b{color:#222;font-weight:600}
.phone{font-size:11px;color:#555}
.phone em{font-style:normal;color:var(--red)}
/* nav */
.nav{left:90px;top:93px;width:634px;height:30px;background:var(--nav);border-bottom:3px solid var(--red);display:flex;align-items:center;justify-content:space-between;padding:0 10px 0 16px;color:#fff;font-size:9px}
.nav .sep{color:#bbb}
/* sidebar */
.browse{left:90px;top:137px;width:153px;border:1px solid var(--line);border-radius:4px;overflow:hidden}
.browse h2{background:var(--red);color:#fff;font-size:11.5px;font-weight:600;height:29px;padding:7px 13px;border-bottom:2px solid var(--red-dark)}
.browse li{list-style:none;height:27.7px;border-top:1px solid var(--line);background:linear-gradient(#fff,#f4f4f4);font-size:8px;font-weight:700;display:flex;justify-content:space-between;align-items:center;padding:0 10px 0 13px;color:#333}
.browse li span{color:#888;font-size:10px;font-weight:400}
/* hero */
.hero{left:254px;top:137px;width:470px;height:251px;background:linear-gradient(110deg,#b77a5a 0%,#d8b9a0 35%,#a36147 60%,#4a3a30 85%,#6d5040 100%)}
.hero-caption{left:254px;top:320px;width:247px;height:68px;background:rgba(40,30,25,.78);color:#fff;font-size:24px;line-height:24px;padding:8px 18px}
.ribbon{left:620px;top:137px;width:104px;height:90px;overflow:hidden}
/* category tiles */
.cat{top:408px;width:201px;height:89px;box-shadow:0 3px 2px -1px #bbb}
.cat .band{position:absolute;left:0;bottom:0;width:100%;height:25px;background:rgba(50,50,55,.85);color:#fff;font-size:15px;font-weight:600;text-align:center;line-height:25px;letter-spacing:.5px}
/* section headings */
.sec-title{font-size:9.5px;font-weight:600;color:#333;top:528px}
.stripes{left:216px;top:529px;width:308px;height:10px;background:repeating-linear-gradient(135deg,#ddd 0 2px,#fff 2px 4px)}
.arrows{top:526px;font-size:11px;font-weight:700;color:#333;letter-spacing:3px}
/* product cards */
.card{width:148px;height:175px;border:1px solid var(--line);box-shadow:0 4px 3px -2px #ccc;background:#fff}
.card .img{position:absolute;left:7px;top:7px;width:136px;height:102px}
.card .name{position:absolute;left:13px;top:120px;font-size:8.5px;color:#555}
.card .cart{position:absolute;left:13px;top:139px;width:57px;height:18px;background:var(--red);border:1.5px solid #f4a3a6;outline:1px solid var(--red);color:#fff;font-size:6.5px;font-weight:700;text-align:center;line-height:15px}
.card .old{position:absolute;left:80px;top:137px;font-size:8.5px;color:#555;text-decoration:line-through}
.card .new-price{position:absolute;left:82px;top:147px;font-size:8.5px;color:var(--red)}
.card .tagnew{position:absolute;left:0;top:0;width:48px;height:48px;overflow:hidden}
.promo{left:580px;width:145px;border:1px solid var(--line);background:#f3f3f3}
.promo .img{position:absolute;left:8px;top:9px;width:128px}
.promo .band{position:absolute;left:8px;width:128px;height:25px;background:rgba(45,45,45,.85);color:#fff;font-size:11.5px;font-weight:600;text-align:center;line-height:25px;letter-spacing:.5px}
/* footer */
.footer{left:95px;top:956px;width:629px;height:209px;background:var(--panel)}
.fcol{top:22px}
.fcol h3{font-size:9px;font-weight:600;color:#333;margin-bottom:22px}
.fcol li{list-style:none;font-size:8px;line-height:12.8px;color:#333}
.frule{left:15px;top:41px;width:598px;height:1px;background:#d6d6d6}
.bottom{left:95px;top:1165px;width:629px;height:35px;background:var(--foot);color:#bbb;font-size:7.5px;text-align:center;line-height:32px}
.chip{position:absolute;height:14px;width:22px;border-radius:2px}
</style>
</head>
<body>
<div class="page"></div>

<header>
  <div class="abs wordmark">LoomNest</div>
  <div class="abs search">Enter a keyword or item</div>
  <div class="abs search-btn">
    <svg width="24" height="24" viewBox="0 0 24 24"><circle cx="11" cy="11" r="4.5" fill="none" stroke="#fff" stroke-width="1.6"/><line x1="14.3" y1="14.3" x2="17.5" y2="17.5" stroke="#fff" stroke-width="1.8"/></svg>
  </div>
  <div class="abs topinfo" style="top:21px">Items (0) &nbsp;<b>Total $0.00</b> &nbsp;View Cart &nbsp;|&nbsp; Checkout</div>
  <div class="abs topinfo phone" style="top:35px">Order Toll-Free &nbsp;: &nbsp;<em>1-800-555-0142</em></div>
  <div class="abs topinfo" style="top:54px">My Account &nbsp;|&nbsp; Sign &nbsp; &#9742; Live Chat &nbsp; &#9679; Online</div>
</header>

<nav class="abs nav">
  <span>Home</span><span class="sep">|</span><span>Selection guides</span><span class="sep">|</span><span>Rug Care</span><span class="sep">|</span><span>FAQ</span><span class="sep">|</span><span>Return Policy</span><span class="sep">|</span><span>Free Shipping</span><span class="sep">|</span><span>Clearance Rugs</span>
</nav>

<aside class="abs browse">
  <h2>Browse</h2>
  <ul>
    <li>RUG THEME<span>+</span></li>
    <li>COLOR WAY<span>+</span></li>
    <li>SIZE<span>+</span></li>
    <li>SHAPE<span>+</span></li>
    <li>FIBER CONTENT<span>+</span></li>
    <li>MFGR. BRAND<span>+</span></li>
    <li>MFGR.COLLECTION<span>+</span></li>
    <li>PRICE<span>+</span></li>
  </ul>
</aside>

<section>
  <div class="abs hero" role="img" aria-label="Close-up photo of a rug's cream fringe on a wooden floor"></div>
  <div class="abs hero-caption">For Domestic and<br>Heirloom values</div>
  <div class="abs ribbon">
    <svg width="104" height="90" viewBox="0 0 104 90">
      <polygon points="20,0 42,0 104,62 104,84" fill="var(--red)"/>
      <text x="0" y="0" transform="translate(37,8) rotate(45)" fill="#fff" font-family="Open Sans, sans-serif" font-size="10">New Arrivals</text>
    </svg>
  </div>
</section>

<section>
  <div class="abs cat" style="left:91px"><div role="img" aria-label="Purple geometric rug" style="position:absolute;inset:0;background:linear-gradient(160deg,#6f4aa8,#4d2f86)"></div><div class="band">TRADITIONAL</div></div>
  <div class="abs cat" style="left:307px"><div role="img" aria-label="Rose patterned rug on a wooden floor" style="position:absolute;inset:0;background:linear-gradient(160deg,#c58c3c,#7a2a1e 55%,#3b1a12)"></div><div class="band">TRANSITIONAL</div></div>
  <div class="abs cat" style="left:523px"><div role="img" aria-label="Cream shag rug" style="position:absolute;inset:0;background:linear-gradient(160deg,#a08a6e,#d9d4bf 50%,#b8b29a)"></div><div class="band">CASUAL</div></div>
</section>

<div class="abs sec-title" style="left:95px">FEATURED PRODUCTS</div>
<div class="abs stripes"></div>
<div class="abs arrows" style="left:542px">&lsaquo;&rsaquo;</div>
<div class="abs sec-title" style="left:580px">YOU MAY ALSO LIKE</div>
<div class="abs arrows" style="left:705px">&lsaquo;&rsaquo;</div>

<section>
  <div class="abs card" style="left:95px;top:558px">
    <div class="img" role="img" aria-label="Black rug with colorful circle pattern" style="background:linear-gradient(135deg,#2a2520,#3a2c22 60%,#8a6a3a)"></div>
    <div class="tagnew"><svg width="48" height="48"><polygon points="0,24 24,0 46,0 0,46" fill="#666"/><text transform="translate(11,31) rotate(-45)" fill="#fff" font-size="8" font-weight="700" font-family="Open Sans, sans-serif">NEW</text></svg></div>
    <div class="name">Lorem Ipsum Dolor</div><div class="cart">ADD TO CART</div><div class="old">$55.67</div><div class="new-price">$48.67</div>
  </div>
  <div class="abs card" style="left:253px;top:558px">
    <div class="img" role="img" aria-label="Gray patterned rug in a modern living room" style="background:linear-gradient(180deg,#777,#ddd 50%,#999)"></div>
    <div class="name">Lorem Ipsum Dolor</div><div class="cart">ADD TO CART</div><div class="old">$55.67</div><div class="new-price">$48.67</div>
  </div>
  <div class="abs card" style="left:412px;top:558px">
    <div class="img" role="img" aria-label="Cream rug with red and black border" style="background:radial-gradient(ellipse at center,#eee3cf 45%,#7a1c18 60%,#1e1a18)"></div>
    <div class="tagnew"><svg width="48" height="48"><polygon points="0,24 24,0 46,0 0,46" fill="#666"/><text transform="translate(11,31) rotate(-45)" fill="#fff" font-size="8" font-weight="700" font-family="Open Sans, sans-serif">NEW</text></svg></div>
    <div class="name">Lorem Ipsum Dolor</div><div class="cart">ADD TO CART</div><div class="old">$55.67</div><div class="new-price">$48.67</div>
  </div>
  <div class="abs card" style="left:95px;top:755px">
    <div class="img" role="img" aria-label="Beige ornate rug on a wooden floor" style="background:linear-gradient(180deg,#b88a5a,#d8cbb0 40%,#a57a4a)"></div>
    <div class="name">Lorem Ipsum Dolor</div><div class="cart">ADD TO CART</div><div class="old">$55.67</div><div class="new-price">$48.67</div>
  </div>
  <div class="abs card" style="left:253px;top:755px">
    <div class="img" role="img" aria-label="Red, gray and white shag rug before a sofa" style="background:linear-gradient(180deg,#ccc,#9a2a2a 40%,#d6d2cc 70%,#555)"></div>
    <div class="tagnew"><svg width="48" height="48"><polygon points="0,24 24,0 46,0 0,46" fill="#666"/><text transform="translate(11,31) rotate(-45)" fill="#fff" font-size="8" font-weight="700" font-family="Open Sans, sans-serif">NEW</text></svg></div>
    <div class="name">Lorem Ipsum Dolor</div><div class="cart">ADD TO CART</div><div class="old">$55.67</div><div class="new-price">$48.67</div>
  </div>
  <div class="abs card" style="left:412px;top:755px">
    <div class="img" role="img" aria-label="Red rug with swirl lines on a wooden floor" style="background:linear-gradient(160deg,#b07a40,#a8201c 40%,#8c1a16 80%,#c69a60)"></div>
    <div class="name">Lorem Ipsum Dolor</div><div class="cart">ADD TO CART</div><div class="old">$55.67</div><div class="new-price">$48.67</div>
  </div>

  <div class="abs promo" style="top:558px;height:175px">
    <div class="img" role="img" aria-label="Striped red and cream rug" style="top:10px;height:155px;background:linear-gradient(180deg,#c8aa88,#7a3a34 45%,#e6dccb 65%,#b89670)"></div>
    <div class="band" style="top:140px">COOL &amp; CALMING</div>
  </div>
  <div class="abs promo" style="top:755px;height:167px">
    <div class="img" role="img" aria-label="Navy and red bordered rug in a room" style="top:10px;height:156px;background:linear-gradient(180deg,#ddd,#2c2f4a 45%,#8a2a22 75%,#c8a27a)"></div>
    <div class="band" style="top:141px">NATURAL RUGS</div>
  </div>
</section>

<footer>
  <div class="abs footer">
    <div class="abs frule"></div>
    <div class="abs fcol" style="left:14px"><h3>Customer Services</h3><ul><li>Shipping</li><li>Return Policy</li><li>Privacy Policy</li><li>Ordering &amp; Delivery</li><li>Checklist</li><li>Terms of Use</li><li>Terms of Sale</li><li>Contact Us</li><li>Environmental Policy</li></ul></div>
    <div class="abs fcol" style="left:145px"><h3>Resources</h3><ul><li>Product Articles</li><li>Learning Center</li><li>Help</li><li>Refer A Friend</li><li>LoomNest Blog</li><li>Room Scene Viewer</li><li>Site Map</li><li>FAQ</li><li>Customer Testimonials</li><li>Photo Gallery</li></ul></div>
    <div class="abs fcol" style="left:268px"><h3>Corporate Info</h3><ul><li>About LoomNest.com</li><li>Careers</li><li>Affiliates</li></ul></div>
    <div class="abs fcol" style="left:400px"><h3>Payments &amp; Security</h3></div>
    <div class="chip" style="left:401px;top:61px;background:#2b3a6b"></div>
    <div class="chip" style="left:426px;top:61px;background:#e7e7e7;border:1px solid #ccc"></div>
    <div class="chip" style="left:451px;top:61px;background:#1a4a9a"></div>
    <div class="chip" style="left:476px;top:61px;background:#3a8ad0"></div>
    <div class="chip" style="left:501px;top:61px;background:#f3c23a"></div>
    <div class="chip" style="left:528px;top:57px;width:82px;height:20px;background:#d9e2ee"></div>
    <div class="abs" style="left:397px;top:94px;width:32px;height:32px;border-radius:50%;background:#e3c25a"></div>
    <div class="abs" style="left:433px;top:94px;width:32px;height:32px;border-radius:50%;background:#f0d060"></div>
    <div class="abs" style="left:470px;top:103px;width:42px;height:16px;background:#ddd;border:1px solid #aaa"></div>
    <div class="abs" style="left:515px;top:101px;width:40px;height:20px;background:#3a5a8a"></div>
    <div class="abs" style="left:558px;top:99px;width:52px;height:24px;background:#e0e0e0;border:1px solid #999"></div>
  </div>
  <div class="abs bottom">© Copyrights 2013 &nbsp;LoomNest. All rights Reserved</div>
</footer>
</body>
</html>
```